Logo/Stationary for Personal Injury Law Firm

We need a logo for our firm and stationary (letterhead, business cards, envelopes) to feature it. We are a personal injury firm that is branching off and starting on our own. Our firm name is "Halvorsen Law, P.C." We would like to take a more modern approach with the design, but still look professional. Our firm takes a very personal approach with all of our clients.
Updates
Here is the info located in the supported file (if you couldnt access it): 4127 North Birchwood Lane Oklahoma City, Oklahoma 73482 Telephone: (405) 362-8140 Fax: (405) 362-8177 Toll Free: (866) 362-8140 Website: www.HalvorsenLaw.example Email: name@halvorsenlaw.example Attorneys: Garrett Halvorsen – licensed to practice in Oklahoma Dustin Pellow – licensed to practice in Oklahoma Of Counsel Cyrus Ponder – licensed to practice in Texas Stefan Ruokola – licensed to practice in New York
Halvorsen Law, P.C.
I have attached an example of the letterhead from our old firm. The main attorneys (Garrett & Dustin) should come first and the of counsel attorneys should be second because they just assist with cases. But please don't let this example box you in to a certain concept.
Target Market(s)
Potential clients involved in personal injury cases (auto accidents, pharmaceutical litigation, medical malpractice & nursing home negligence).
Industry/Entity Type
Lawyer
Requirements
Must have
- Logo - Firm name "Halvorsen Law, P.C."
- Letterhead - Please see the supporting file containing all the information that needs to be presented.
- Business Card - name, title (attorney/legal assistant), address, telephone, fax, email, website
- Envelope - Logo and address
Should not have
- All of the attorneys are male, so we aren''t interested in any feminine designs.
- Please do not use any scales, gavels or family crest designs.

```html
<!DOCTYPE html>
<html lang="en">
<head>
<meta charset="utf-8">
<title>Halvorsen Law, P.C. — Stationery</title>
<link href="https://fonts.googleapis.com/css2?family=Tinos:wght@400;700&display=swap" rel="stylesheet">
<style>
  :root {
    --ink: #231f20;
    --paper: #ffffff;
    --frame: #4a4a4a;
    --sun: #f5a623;
  }
  * { margin: 0; padding: 0; box-sizing: border-box; }
  html, body { width: 1176px; height: 1200px; overflow: hidden; background: var(--paper); }
  body { position: relative; font-family: "Tinos", "Times New Roman", serif; color: var(--ink); }
  .abs { position: absolute; white-space: nowrap; line-height: 1; }
  .mark { position: absolute; border-radius: 50%; background: var(--sun); }
  .firm-name { position: absolute; white-space: nowrap; line-height: 1; font-weight: 400; color: var(--ink); letter-spacing: 0.02em; }

  .card { position: absolute; left: 85px; width: 305px; height: 172px; border: 1px solid var(--frame); border-radius: 8px; background: var(--paper); }
  .card--front-1 { top: 363px; }
  .card--back { top: 556px; }
  .card--front-2 { top: 749px; }
  .card .address { left: 15px; font-size: 5.6px; letter-spacing: 0.12em; }
  .card .person { font-size: 17px; font-weight: 700; }
  .card .contact { left: 165px; top: 106px; font-size: 7.6px; line-height: 9.2px; white-space: nowrap; position: absolute; }

  .letterhead { position: absolute; left: 430px; top: 294px; width: 660px; height: 840px; border: 1px solid var(--frame); background: var(--paper); }
  .letterhead .address { left: 40px; font-size: 9px; letter-spacing: 0.22em; }
  .letterhead .contact { position: absolute; left: 436px; top: 68px; font-size: 12px; line-height: 12.6px; white-space: nowrap; }
  .letterhead .roster { position: absolute; left: 52px; top: 682px; font-size: 11.5px; line-height: 10.6px; white-space: nowrap; }
  .letterhead .roster p + p { margin-top: 0; }
  .letterhead .roster .gap { margin-top: 10px; }
  .letterhead .footnote { left: 40px; top: 797px; font-size: 11px; }
</style>
</head>
<body>

  <!-- Main logo lockup -->
  <div class="mark" style="left:232px; top:67px; width:112px; height:112px;"></div>
  <div class="firm-name" style="left:98px; top:206px; font-size:50px;">Halvorsen Law, P.C.</div>

  <!-- Business card: Garrett Halvorsen -->
  <div class="card card--front-1">
    <div class="mark" style="left:50px; top:13px; width:30px; height:30px;"></div>
    <div class="firm-name" style="left:15px; top:46px; font-size:14px;">Halvorsen Law, P.C.</div>
    <div class="abs address" style="top:64px;">4127 North Birchwood Lane</div>
    <div class="abs address" style="top:71px;">Oklahoma City, Oklahoma 73482</div>
    <div class="abs person" style="left:152px; top:75px;">Garrett Halvorsen</div>
    <div class="contact">
      Telephone: (405) 362-8140<br>
      Fax: (405) 362-8177<br>
      Toll Free: (866) 362-8140<br>
      Website: www.HalvorsenLaw.example<br>
      Email: name@halvorsenlaw.example
    </div>
  </div>

  <!-- Business card: back -->
  <div class="card card--back">
    <div class="mark" style="left:94px; top:28px; width:62px; height:62px;"></div>
    <div class="firm-name" style="left:27px; top:104px; font-size:22px;">Halvorsen Law, P.C.</div>
  </div>

  <!-- Business card: Dustin Pellow -->
  <div class="card card--front-2">
    <div class="mark" style="left:50px; top:13px; width:30px; height:30px;"></div>
    <div class="firm-name" style="left:15px; top:46px; font-size:14px;">Halvorsen Law, P.C.</div>
    <div class="abs address" style="top:64px;">4127 North Birchwood Lane</div>
    <div class="abs address" style="top:71px;">Oklahoma City, Oklahoma 73482</div>
    <div class="abs person" style="left:137px; top:75px;">Dustin Pellow</div>
    <div class="contact">
      Telephone: (405) 362-8140<br>
      Fax: (405) 362-8177<br>
      Toll Free: (866) 362-8140<br>
      Website: www.HalvorsenLaw.example<br>
      Email: name@halvorsenlaw.example
    </div>
  </div>

  <!-- Letterhead -->
  <div class="letterhead">
    <div class="mark" style="left:95px; top:24px; width:60px; height:60px;"></div>
    <div class="firm-name" style="left:40px; top:81px; font-size:21px;">Halvorsen Law, P.C.</div>
    <div class="abs address" style="top:106px;">4127 North Birchwood Lane</div>
    <div class="abs address" style="top:117px;">Oklahoma City, Oklahoma 73482</div>
    <div class="contact">
      Telephone: (405) 362-8140<br>
      Fax: (405) 362-8177<br>
      Toll Free: (866) 362-8140<br>
      Website: www.HalvorsenLaw.example<br>
      Email: name@halvorsenlaw.example
    </div>
    <div class="roster">
      <p>Attorneys:</p>
      <p class="gap">Garrett Halvorsen – licensed to practice in Oklahoma</p>
      <p>Dustin Pellow – licensed to practice in Oklahoma</p>
      <p class="gap">Of Counsel</p>
      <p class="gap">Cyrus Ponder – licensed to practice in Texas</p>
      <p>Stefan Ruokola – licensed to practice in New York</p>
    </div>
    <div class="abs footnote">*Licensed to Practice in Oklahoma and New Jersey &nbsp;+Licensed to practice in New York &nbsp;†Licensed to practice in Texas</div>
  </div>

</body>
</html>
```